HARLOW COLLEGE INFOMATION BOOKLET

WE NEED TO DESIGN OUR COLLEGE INFORMATION BOOKLET
WHICH WE GIVE TO STUDENTS LOOKING AT ENROLLING IN OUR COLLEGE, THIS WILL INCLUDE OUR COURSES WE OFFER, COLLEGE INFORMATION , STUDENT TESTIMONIAL ETC, WE GIVE THISS BOOK OUT AT TRADE SHOWS SO IT NEED TO BE GREAT. VIEW OUR WEBSITE
WWW.HARLOWCOLLEGE.EXAMPLE.AU

Target Market(s)

INTERNATIONAL STUDENTS FROM AROUND THE WORLD

Industry/Entity Type

Education

Requirements
Must have
• OUR LOGO

```html
<!DOCTYPE html>
<html lang="en">
<head>
<meta charset="utf-8">
<title>Quillmoor College – Student Services</title>
<link rel="stylesheet" href="https://fonts.googleapis.com/css2?family=Bebas+Neue&family=Open+Sans:wght@400;600;700&display=swap">
<style>
  :root {
    --navy: #1d3550;
    --sky: #1c9ad6;
    --text: #3a3a3a;
    --bullet: #9a9ea3;
    --band: #29a8df;
    --page: #ffffff;
  }
  * { margin: 0; padding: 0; box-sizing: border-box; }
  html, body { width: 847px; height: 1200px; overflow: hidden; background: var(--page); }
  .page { position: relative; width: 847px; height: 1200px; background: var(--page); font-family: "Open Sans", Arial, sans-serif; color: var(--text); }

  .hero-photo {
    position: absolute; left: 0; top: 0; width: 847px; height: 248px;
    background: linear-gradient(100deg, #7fae5a 0%, #c9d9c4 30%, #d8c2b0 52%, #e9edf2 75%, #cdd9e6 100%);
  }

  .intro { position: absolute; left: 31px; top: 278px; width: 790px; }
  .section-title {
    position: relative; padding-left: 20px;
    font-family: "Bebas Neue", "Arial Narrow", sans-serif; font-weight: 400;
    font-size: 40px; line-height: 40px; color: var(--navy); letter-spacing: 0.3px;
  }
  .section-title::before {
    content: ""; position: absolute; left: 0; top: 4px; width: 6px; height: 30px; background: var(--sky);
  }
  .section-subtitle {
    padding-left: 20px;
    font-family: "Bebas Neue", "Arial Narrow", sans-serif; font-weight: 400;
    font-size: 27px; line-height: 28px; color: var(--sky); letter-spacing: 0.4px;
  }
  .lead, .contact { padding-left: 20px; font-size: 14.5px; line-height: 20px; font-weight: 400; letter-spacing: 0.35px; color: var(--text); }
  .lead { margin-top: 22px; }
  .contact { margin-top: 18px; }
  .contact strong { font-weight: 700; }

  .support { position: absolute; left: 51px; top: 538px; width: 770px; }
  .support-title {
    font-family: "Bebas Neue", "Arial Narrow", sans-serif; font-weight: 400;
    font-size: 36px; line-height: 36px; color: var(--sky); letter-spacing: 0.4px;
  }
  .service-list { list-style: none; margin-top: 16px; }
  .service-list li {
    position: relative; padding-left: 28px; font-size: 15.5px; line-height: 19px; margin-bottom: 11.3px; letter-spacing: 0.6px; color: var(--text);
  }
  .service-list li::before {
    content: ""; position: absolute; left: 0; top: 4px; width: 11px; height: 11px; background: var(--bullet);
  }

  .footer-band { position: absolute; left: 0; bottom: 0; width: 847px; height: 57px; background: var(--band); }
</style>
</head>
<body>
<div class="page">
  <div class="hero-photo" role="img" aria-label="Photograph of a smiling group of college students standing outdoors in front of a campus building"></div>

  <section class="intro">
    <h1 class="section-title">STUDENT SERVICES</h1>
    <h2 class="section-subtitle">OUR FRIENDLY STAFF VALUES OUR STUDENTS</h2>
    <p class="lead">Quillmoor College Offers Guidance and Counselling to All of Our Students to Help Them Find Work, Accommodation, and Answer Any Questions About Their Studies.</p>
    <p class="contact">Please contact the College on (International) <strong>+61 7 5550 1200</strong>, or (Local) <strong>07 5550 1200</strong>, or <strong>email to admin@quillmoorcollege.example.au</strong> if you have any questions about the following; you can also access this and other important information through your Student Handbook.</p>
  </section>

  <section class="support">
    <h2 class="support-title">STUDENT SUPPORT SERVICES</h2>
    <ul class="service-list">
      <li>Applying for an international student visa</li>
      <li>Student welfare and guidance</li>
      <li>Change of address and other personal information</li>
      <li>Overseas student health</li>
      <li>Accommodation</li>
      <li>Life in Australia</li>
      <li>Fees and refunds</li>
      <li>Enrolment and orientation</li>
      <li>Reasonable adjustment of assessment</li>
      <li>Language, literacy and numeracy assistance</li>
      <li>Academic performance</li>
      <li>Extension and re-assessment</li>
      <li>Confidentiality, security and access to your records</li>
      <li>Recognition of prior learning and credit transfer</li>
      <li>Critical incidents</li>
      <li>Airport transfers to your accommodation which can be arranged for a small fee</li>
      <li>School Aged Dependent Children – International Students only</li>
    </ul>
  </section>

  <div class="footer-band"></div>
</div>
</body>
</html>
```